Crowdsourced IT recruitment agency - velmorix

We need an engaging and smart website design for VELMORIX Crowd recruitment. We are young innovative IT recruitment company. We have deep expertise in all IT & digital areas and using crowdsourcing to search the best market candidates faster than ever.
Our mission: to connect people and organizations interests, inspiring each other and enabling together reach better results.

We would like the design to be personalized, emotional, yet simple and neat. It should focus on the person with a problem which we solve.

Reading the site customers should feel safe and confident that velmorix is the trusted partner and everything we do is a quality product.

We also focus on long term relationship with our clients.

We have 4 products:
IT Recruitment – professional recruitment of candidates in IT and digital areas
IT RPO – candidates research process outsourcing(RPO) - provision of resume pools for the client
Kestrel Talent School – training, seminars and networking events for HR professionals from IT and hi-tech companies
Plumview Board – a tool for data visualization in nice and interactive dashboards. It pulls data from different corporate sources (SAP, Oracle, excel, etc.). It looks like a dashboard, on which there are several graphs or diagrams with HR and business KPIs(key performance indicators)

We like material design sites but also open for other options/ideas

Current site velmorix-hire.ru

Examples of websites that we like:
http://www.quobrant.ru
https://dunmirecardio.ru

Site structure:
About us (description, mission, team, clients, office)
Products: Plumview Board, HR IPO, It Recruitment
Kestrel Talent School (list of events (past and future) with the ability to upload photos, descriptions, etc.)
News: Publications, Articles, Blog
Contacts

Industry/Entity Type

Consulting

Number of Pages Required

5+ page

Font styles to use
Serif
Sans Serif

Requirements
Must have
• Individual blocks with the transition to a separate page for each product
• Link to social network (fb, link),
• Subscribe to news on the main page
• Feedback form
• Site structure:
• About us (description, mission, team, clients, office)
• Products: Plumview Board, HR IPO, It Recruitment
• Kestrel Talent School (list of events (past and future) with the ability to upload photos, descriptions, etc.)
• News: Publications, Articles, Blog, Calendars
• Contacts
Should not have
• too crowded
• too complicatied
• without advertising banners
• crammed

```html
<!DOCTYPE html>
<html lang="en">
<head>
<meta charset="utf-8">
<title>VELMORIX Crowd recruitment</title>
<link rel="stylesheet" href="https://fonts.googleapis.com/css2?family=Questrial&family=Montserrat:wght@700&display=swap">
<style>
  :root {
    --sky-top: #a3dcea;
    --sky-bottom: #92cedd;
    --brand-blue: #0062a7;
    --brand-deep: #0a4f8c;
    --brand-top: #03559a;
    --accent-blue: #1a88c9;
    --ink-dark: #1f2a33;
    --white: #ffffff;
    --side-top: #e3e3df;
    --rule: rgba(255,255,255,0.55);
  }
  * { margin: 0; padding: 0; box-sizing: border-box; }
  html, body { width: 1200px; height: 566px; overflow: hidden; }
  body {
    position: relative;
    background: linear-gradient(180deg, var(--sky-top), var(--sky-bottom));
    font-family: "Questrial", "Century Gothic", sans-serif;
    color: var(--white);
  }
  .site-header { position: absolute; left: 73px; top: 0; width: 1063px; height: 111px; border-bottom: 1px solid var(--rule); }
  .brand { position: absolute; left: 0; top: 26px; display: flex; align-items: center; gap: 14px; text-decoration: none; }
  .brand-mark { width: 58px; height: 58px; border-radius: 50%; background: var(--brand-blue); }
  .brand-name { font-family: "Questrial", sans-serif; font-size: 30px; line-height: 30px; color: var(--brand-deep); }
  .main-nav { position: absolute; left: 394px; top: 50px; display: flex; }
  .main-nav a { color: var(--white); text-decoration: none; font-size: 14px; white-space: nowrap; text-shadow: 0 1px 1px rgba(0,0,0,0.25); }
  .nav-about { width: 96px; } .nav-products { width: 97px; } .nav-school { width: 162px; } .nav-news { width: 97px; } .nav-contact { width: 100px; }
  .social { position: absolute; left: 928px; top: 51px; display: flex; gap: 9px; }
  .social a { display: flex; align-items: center; gap: 4px; color: var(--white); text-decoration: none; font-size: 11px; }
  .social a::before { content: ""; width: 10px; height: 10px; border-radius: 50%; background: var(--white); }
  .hero-copy { position: absolute; left: 73px; top: 212px; width: 470px; }
  .mission { font-size: 25.5px; line-height: 32.5px; color: var(--white); text-shadow: 0 1px 2px rgba(0,0,0,0.25); }
  .mission strong { font-family: "Montserrat", sans-serif; font-weight: 700; font-size: 22.5px; }
  .word-connect { color: var(--brand-deep); }
  .word-inspiring { color: var(--ink-dark); }
  .word-together { color: var(--accent-blue); }
  .read-more { display: inline-block; margin-top: 20px; color: var(--brand-deep); text-decoration: none; font-size: 22px; }
  .product-steps { position: absolute; left: 466px; top: 184px; }
  .product-steps text { font-family: "Questrial", sans-serif; }
</style>
</head>
<body>
  <header class="site-header">
    <a class="brand" href="#">
      <span class="brand-mark"></span>
      <span class="brand-name">velmorix</span>
    </a>
    <nav class="main-nav">
      <a class="nav-about" href="#">About Us</a>
      <a class="nav-products" href="#">Products</a>
      <a class="nav-school" href="#">Kestrel Talent School</a>
      <a class="nav-news" href="#">News</a>
      <a class="nav-contact" href="#">Contact Us</a>
    </nav>
    <div class="social">
      <a href="#">Pixora</a>
      <a href="#">Snapvale</a>
      <a href="#">Chirpnet</a>
    </div>
  </header>

  <section class="hero-copy">
    <p class="mission">To <strong class="word-connect">connect</strong> people and organizations interests, <strong class="word-inspiring">inspiring</strong> each other and enabling <strong class="word-together">together</strong> reach better results.</p>
    <a class="read-more" href="#">Read More</a>
  </section>

  <svg class="product-steps" width="670" height="306" viewBox="0 0 670 306" aria-label="Products">
    <g class="step-recruitment">
      <polygon points="92,12 100,0 486,0 514,12" fill="var(--brand-top)"/>
      <polygon points="514,12 486,0 610,0 668,12" fill="var(--side-top)"/>
      <rect x="92" y="12" width="422" height="142" fill="var(--brand-blue)"/>
      <rect x="514" y="12" width="154" height="142" fill="var(--white)"/>
      <text x="303" y="80" fill="var(--white)" font-size="18" text-anchor="middle">Professional Recruitment of Candidates in</text>
      <text x="303" y="100" fill="var(--white)" font-size="18" text-anchor="middle">IT and Digital areas</text>
      <text x="591" y="86" fill="var(--brand-blue)" font-size="33" text-anchor="middle">IT</text>
      <text x="591" y="115" fill="var(--brand-blue)" font-size="23" text-anchor="middle">Recruitment</text>
    </g>
    <g class="step-rpo">
      <polygon points="0,172 30,160 400,160 424,172" fill="var(--brand-top)"/>
      <polygon points="424,172 400,160 530,160 577,172" fill="var(--side-top)"/>
      <rect x="0" y="172" width="424" height="130" fill="var(--brand-blue)"/>
      <rect x="424" y="172" width="153" height="130" fill="var(--white)"/>
      <text x="212" y="225" fill="var(--white)" font-size="18" text-anchor="middle">candidates research process outsourcing(RPO)</text>
      <text x="212" y="245" fill="var(--white)" font-size="18" text-anchor="middle">provision of resume pools for the client</text>
      <text x="500" y="233" fill="var(--brand-blue)" font-size="33" text-anchor="middle">IT</text>
      <text x="500" y="258" fill="var(--brand-blue)" font-size="22" text-anchor="middle">RPO</text>
    </g>
  </svg>
</body>
</html>
```